Verantix - Solution provider in business consulting

Verantix is a swiss based company providing solutions for developing markets. The business covers various fields of business consulting, such as supply chain, product costs, quality management and manufacturing management. The Business operates in a efficient, straight and solution oriented manner.
The final design should communicate these characteristics. Asian people as well as as western people shall identify the qualities of the company at first sight.
The customer needs business cards with a simple view but an recognizable design, printed in high quality. Engraved elements such as the globe or simple words are possible.
Available colors are: (RAL)
102/102/102
51/102/102
153/204/153
255/102/51
Font: Calibri
Industry/Entity Type
Business
Look and feel
Each slider illustrates characteristics of the customer's brand and the style your logo design should communicate.

```html
<!DOCTYPE html>
<html lang="en">
<head>
<meta charset="utf-8">
<title>Verantix Business Cards</title>
<link href="https://fonts.googleapis.com/css2?family=Carlito:wght@400;700&display=swap" rel="stylesheet">
<style>
  :root {
    --backdrop: #e9e7e3;
    --card-dark: #666666;
    --card-light: #ffffff;
    --ink: #5a5a5a;
    --ink-soft: #6e6e6e;
    --on-dark: #ffffff;
    --shadow: rgba(0, 0, 0, 0.18);
  }
  * { margin: 0; padding: 0; box-sizing: border-box; }
  html, body {
    width: 1200px;
    height: 900px;
    overflow: hidden;
    background: var(--backdrop);
    font-family: "Carlito", "Calibri", sans-serif;
  }
  .stage {
    position: relative;
    width: 1200px;
    height: 900px;
  }
  .card {
    position: absolute;
    width: 580px;
    height: 350px;
    border-radius: 3px;
    box-shadow: 0 10px 28px var(--shadow);
  }
  .card--back {
    left: 110px;
    top: 120px;
    background: var(--card-dark);
  }
  .card--front {
    left: 510px;
    top: 420px;
    background: var(--card-light);
  }
  .back-wordmark {
    position: absolute;
    left: 60px;
    bottom: 70px;
    color: var(--on-dark);
    font-size: 76px;
    font-weight: 400;
    letter-spacing: 1px;
    line-height: 1;
  }
  .front-logo {
    position: absolute;
    left: 40px;
    top: 52px;
    display: flex;
    align-items: center;
    gap: 12px;
  }
  .front-logo__mark {
    width: 40px;
    height: 40px;
    border-radius: 50%;
    background: var(--card-dark);
  }
  .front-logo__name {
    color: var(--ink);
    font-size: 44px;
    font-weight: 400;
    line-height: 1;
  }
  .contact {
    position: absolute;
    left: 345px;
    top: 42px;
    color: var(--ink);
  }
  .contact__name {
    font-size: 19px;
    font-weight: 700;
  }
  .contact__role {
    font-size: 13px;
    margin: 2px 0 0 8px;
  }
  .contact__address {
    font-size: 13px;
    line-height: 1.25;
    margin: 18px 0 0 28px;
    color: var(--ink-soft);
  }
  .contact__list {
    list-style: none;
    margin: 18px 0 0 50px;
    font-size: 14px;
    color: var(--ink-soft);
  }
  .contact__list li {
    display: flex;
    align-items: center;
    gap: 10px;
    line-height: 1.45;
  }
  .contact__icon {
    width: 12px;
    height: 12px;
    flex: none;
    fill: var(--ink-soft);
  }
</style>
</head>
<body>
<main class="stage">
  <section class="card card--back" aria-label="Card back">
    <p class="back-wordmark">verantix</p>
  </section>

  <section class="card card--front" aria-label="Card front">
    <div class="front-logo">
      <span class="front-logo__name">verantix</span>
      <span class="front-logo__mark" aria-hidden="true"></span>
    </div>

    <div class="contact">
      <p class="contact__name">Lukas Wendel</p>
      <p class="contact__role">CEO</p>
      <p class="contact__address">Verantix GmbH Feldrain 8<br>9400 Talbach Switzerland</p>
      <ul class="contact__list">
        <li>
          <svg class="contact__icon" viewBox="0 0 12 12" aria-hidden="true"><rect x="3" y="0.5" width="6" height="11" rx="1" fill="none" stroke="currentColor" stroke-width="1.2" style="stroke:var(--ink-soft)"/><rect x="5" y="9" width="2" height="1"/></svg>
          +41 79 382 5071
        </li>
        <li>
          <svg class="contact__icon" viewBox="0 0 12 12" aria-hidden="true"><path d="M2.5 1 L4.5 1 L5.3 3.6 L4 4.6 C4.7 6.1 5.9 7.3 7.4 8 L8.4 6.7 L11 7.5 L11 9.5 C11 10.3 10.3 11 9.5 11 C5 11 1 7 1 2.5 C1 1.7 1.7 1 2.5 1 Z"/></svg>
          +41 71 604 2938
        </li>
        <li>
          <svg class="contact__icon" viewBox="0 0 12 12" aria-hidden="true"><rect x="0.5" y="2" width="11" height="8" rx="1"/><path d="M1 2.8 L6 6.6 L11 2.8" fill="none" stroke="#ffffff" stroke-width="1"/></svg>
          lukas.wendel@verantix.ch
        </li>
        <li>
          <svg class="contact__icon" viewBox="0 0 12 12" aria-hidden="true"><circle cx="6" cy="6" r="5.5"/><path d="M0.5 6 H11.5 M6 0.5 C3.5 3 3.5 9 6 11.5 M6 0.5 C8.5 3 8.5 9 6 11.5" fill="none" stroke="#ffffff" stroke-width="0.8"/></svg>
          www.verantix.ch
        </li>
      </ul>
    </div>
  </section>
</main>
</body>
</html>
```